LinkedIn Engagement Posts for Bookkeeping Company

The task is to complete 20 engaging posts for our LinkedIn page. These posts should ask a question, take a poll, provide useful information or interesting articles. These should NOT be advertisements for our services. Our target audience is business owners (small and mid-size businesses). The content should be relevant to business owners/entrepreneurs. Topics should include content about making money, accounting/bookkeeping info, operating a business, cashflow, etc.

We use QuickBooks Online for our services, so do not refer to any other accounting software (unless it is a comparison showing advantages of QBO).

Our website:
https://www.fernhollowaccounting.com/

Target Market(s)

Business owners/entrepreneurs (Small & Mid-Sized Businesses)

Industry/Entity Type

Accounting company that provides bookkeeping services, financial reporting and payroll processing (does not provide tax services!)

Font styles to use
Serif
Sans Serif

Colors
0054AA
0677BA
7BADD7
CADEEF
E8F1F8

Requirements
Must have
• 20 Engaging posts for LinkedIn, including hashtags
Nice to have
• Stay with current branding for overall design graphics (see website and social media accounts)
Should not have
• We do not provide tax or audit services, so please do not include these topics other that to say you must have accurate and updated bookkeeping in order to complete taxes and/or in the event of an audit.

```html
<!DOCTYPE html>
<html lang="en">
<head>
<meta charset="UTF-8">
<title>Behind every business there is great financial management</title>
<link rel="stylesheet" href="https://fonts.googleapis.com/css2?family=Roboto:wght@400;700;900&display=swap">
<style>
  :root {
    --bg-deep: #0b3a84;
    --bg-mid: #0f4fa8;
    --bg-bright: #1766c2;
    --panel: #0b2d66;
    --ring: rgba(7, 30, 80, 0.28);
    --white: #ffffff;
    --gold: #f7b500;
    --rule: rgba(255, 255, 255, 0.75);
  }
  * { margin: 0; padding: 0; box-sizing: border-box; }
  html, body {
    width: 1200px;
    height: 627px;
    overflow: hidden;
  }
  .post {
    position: relative;
    width: 1200px;
    height: 627px;
    overflow: hidden;
    background: linear-gradient(100deg, var(--bg-deep) 0%, var(--bg-mid) 55%, var(--bg-bright) 100%);
    font-family: "Roboto", Arial, sans-serif;
  }
  .rings {
    position: absolute;
    inset: 0;
  }
  .headline-panel {
    position: absolute;
    left: 38px;
    top: 50px;
    width: 524px;
    height: 540px;
    background: var(--panel);
    border-radius: 42px;
    text-align: center;
    color: var(--white);
  }
  .brand {
    position: absolute;
    top: 68px;
    left: 0;
    right: 0;
    display: flex;
    align-items: center;
    justify-content: center;
    gap: 10px;
    font-weight: 700;
    font-size: 24px;
    color: var(--white);
  }
  .brand-mark {
    width: 16px;
    height: 16px;
    background: var(--white);
  }
  .divider {
    position: absolute;
    top: 150px;
    left: 59px;
    width: 396px;
    height: 1px;
    background: var(--rule);
  }
  .headline {
    font-weight: 400;
  }
  .headline .line {
    position: absolute;
    left: 0;
    right: 0;
    display: block;
    line-height: 1;
    white-space: nowrap;
  }
  .headline .plain {
    font-weight: 400;
    font-size: 58px;
    letter-spacing: -0.5px;
  }
  .headline .accent {
    font-weight: 900;
    font-size: 58px;
    color: var(--gold);
    letter-spacing: 1px;
  }
  .line-1 { top: 176px; }
  .line-2 { top: 251px; }
  .line-3 { top: 316px; }
  .line-4 { top: 390px; }
  .line-5 { top: 451px; }
  .illustration {
    position: absolute;
    left: 612px;
    top: 205px;
    width: 588px;
    height: 335px;
    border-radius: 46% 38% 30% 44% / 48% 36% 40% 42%;
    background:
      radial-gradient(ellipse 130px 110px at 230px 240px, rgba(247, 181, 0, 0.85), rgba(247, 181, 0, 0) 100%),
      radial-gradient(ellipse 110px 150px at 380px 200px, rgba(24, 38, 70, 0.85), rgba(24, 38, 70, 0) 100%),
      radial-gradient(ellipse 90px 130px at 80px 200px, rgba(240, 90, 120, 0.7), rgba(240, 90, 120, 0) 100%),
      radial-gradient(ellipse 120px 140px at 520px 220px, rgba(140, 215, 210, 0.75), rgba(140, 215, 210, 0) 100%),
      radial-gradient(ellipse 280px 170px at 300px 180px, rgba(180, 220, 235, 0.35), rgba(180, 220, 235, 0) 100%);
  }
</style>
</head>
<body>
  <main class="post">
    <svg class="rings" width="1200" height="627" viewBox="0 0 1200 627" aria-hidden="true">
      <circle cx="1060" cy="390" r="190" fill="none" stroke="var(--ring)" stroke-width="55"/>
      <circle cx="1060" cy="390" r="330" fill="none" stroke="var(--ring)" stroke-width="55"/>
      <circle cx="1060" cy="390" r="470" fill="none" stroke="var(--ring)" stroke-width="55"/>
    </svg>

    <section class="headline-panel">
      <div class="brand">
        <span class="brand-mark"></span>
        <span class="brand-name">Fern Hollow Accounting</span>
      </div>
      <div class="divider"></div>
      <h1 class="headline">
        <span class="line plain line-1">Behind every</span>
        <span class="line accent line-2">BUSINESS</span>
        <span class="line plain line-3">There is a Great</span>
        <span class="line accent line-4">FINANCIAL</span>
        <span class="line accent line-5">MANAGEMENT</span>
      </h1>
    </section>

    <div class="illustration" role="img" aria-label="Illustration of a team working around a large calculator with stacked gold coins, banknotes and a rising bar chart"></div>
  </main>
</body>
</html>
```